Book Cover for a short book on cryptocurrency investment

I need a cover design for a book titled "Quiet Rivers of the Hollow Orchard" with the subtitle "A Patient Wandering". The book will be freely distributed as well as available on Brindlemart. I am open to any design concept that peaks my interest. My only suggestion would be to make the design colorful, bright, and attractive but this is not set in stone. I would also like to avoid pictures of coins or crypto logos if possible.

```html
<!DOCTYPE html>
<html lang="en">
<head>
<meta charset="utf-8">
<title>Quiet Rivers of the Hollow Orchard — Book Cover</title>
<link href="https://fonts.googleapis.com/css2?family=Cinzel:wght@400;500&display=swap" rel="stylesheet">
<style>
  :root {
    --cover-black: #050607;
    --ink-white: #f4f4f2;
    --glow-teal: #2fc9c4;
    --glow-blue: #3d5fd6;
    --glow-deep: #0d2f4a;
  }
  html, body {
    margin: 0;
    padding: 0;
    width: 751px;
    height: 1200px;
    overflow: hidden;
    background: var(--cover-black);
  }
  .book-cover {
    position: relative;
    width: 751px;
    height: 1200px;
    background: var(--cover-black);
    color: var(--ink-white);
    font-family: "Cinzel", serif;
    overflow: hidden;
  }
  .author-name {
    position: absolute;
    top: 54px;
    left: 0;
    width: 100%;
    margin: 0;
    text-align: center;
    font-size: 38px;
    font-weight: 400;
    letter-spacing: 0.62em;
    text-indent: 0.62em;
    text-transform: uppercase;
    line-height: 1;
  }
  .book-title {
    position: absolute;
    top: 225px;
    left: 0;
    width: 100%;
    margin: 0;
    text-align: center;
    font-size: 70px;
    font-weight: 400;
    line-height: 98px;
    letter-spacing: 0.01em;
  }
  .book-title span { display: block; }
  .book-subtitle {
    position: absolute;
    top: 588px;
    left: 0;
    width: 100%;
    margin: 0;
    text-align: center;
    font-size: 32px;
    font-weight: 400;
    letter-spacing: 0.02em;
    line-height: 1;
  }
  .cover-artwork {
    position: absolute;
    left: 0;
    top: 630px;
    width: 751px;
    height: 570px;
    display: block;
  }
</style>
</head>
<body>
  <main class="book-cover">
    <p class="author-name">Tomas Verel</p>
    <h1 class="book-title">
      <span>Quiet Rivers</span>
      <span>of the Hollow</span>
      <span>Orchard</span>
    </h1>
    <p class="book-subtitle">A Patient Wandering</p>

    <svg class="cover-artwork" viewBox="0 0 751 570" role="img"
         aria-label="Glowing digital rings of light in teal and blue surrounding a faceted crystal shape">
      <defs>
        <radialGradient id="artGlow" cx="50%" cy="62%" r="55%">
          <stop offset="0" stop-color="var(--glow-blue)" stop-opacity="0.95"/>
          <stop offset="0.28" stop-color="var(--glow-teal)" stop-opacity="0.75"/>
          <stop offset="0.62" stop-color="var(--glow-deep)" stop-opacity="0.55"/>
          <stop offset="1" stop-color="var(--cover-black)" stop-opacity="0"/>
        </radialGradient>
      </defs>
      <rect x="0" y="0" width="751" height="570" fill="url(#artGlow)"/>
    </svg>
  </main>
</body>
</html>
```